Media Kit

We're a editorial website that enjoys some love from advertisers and publicists.
We need a digital media kit (probably in PDF form) that tells a story about who we are, who our readers are, our traffic and so forth.
The copy and a logo file are attached - you just need to make it look awesome. Our logo font is 'elephant'. Our secondary font is Futura Lt Bt.
To get a sense of the types of media kits in the market, check out:
http://www.novapresskit.example/hotdata/publishers/novapk/advertiser/4471902/5530617/MediaKitFinal_2013.pdf
http://www.bluelantern84.example/static/corporate/images/3f912a/corporate/assets/bl84_mediakit.pdf
Or look to other traditional and digital magazines in the lifestyle space.
Please note: we will require the original artwork files from the successful designer.
Updates
If you wish, a sample rather than the whole project is fine to secure payment.
Target Market(s)
Publicists, Marketing Managers, Media Buyers
Industry/Entity Type
Digital
Look and feel
Each slider illustrates characteristics of the customer's brand and the style your logo design should communicate.

```html
<!DOCTYPE html>
<html lang="en">
<head>
<meta charset="utf-8">
<title>The Velvet Quarter – Media Kit</title>
<link rel="stylesheet" href="https://fonts.googleapis.com/css2?family=Playfair+Display:wght@400;700;900&display=swap">
<style>
  :root {
    --backdrop: #2a2a2a;
    --paper: #ffffff;
    --ink: #111111;
    --muted: #9a9a9a;
    --soft: #c9c9c9;
    --photo-light: #e9e6e3;
    --photo-mid: #b89a86;
    --photo-dark: #6d4f3f;
    --serif: "Playfair Display", "Bodoni 72", Georgia, serif;
  }
  * { box-sizing: border-box; margin: 0; padding: 0; }
  html, body { width: 1200px; height: 1000px; overflow: hidden; }
  body { background: var(--backdrop); font-family: var(--serif); color: var(--ink); position: relative; }

  .page { position: absolute; background: var(--paper); overflow: hidden; }
  .page--cover   { left: 410px; top: 282px; width: 385px; height: 271px; }
  .page--about   { left: 62px;  top: 300px; width: 316px; height: 250px; }
  .page--stats   { left: 825px; top: 300px; width: 316px; height: 250px; }
  .page--network { left: 503px; top: 722px; width: 300px; height: 210px; }
  .page--contact { left: 827px; top: 722px; width: 300px; height: 210px; }

  .brand { position: absolute; left: 16px; top: 16px; display: flex; align-items: center; gap: 4px; }
  .brand__dot { width: 22px; height: 22px; border-radius: 50%; background: var(--ink); }
  .brand__name { font-size: 4.5px; font-weight: 700; color: var(--ink); white-space: nowrap; }

  .heading { position: absolute; font-size: 11px; font-weight: 900; line-height: 1; }
  .copy { position: absolute; font-size: 4.4px; line-height: 1.4; color: var(--muted); font-weight: 700; }
  .copy p { margin-bottom: 4px; }
  .copy b { color: var(--ink); font-weight: 900; font-size: 5.6px; }

  /* cover */
  .cover__photo { position: absolute; inset: 0;
    background: radial-gradient(ellipse at 50% 45%, var(--photo-mid) 0%, #cfc4bc 35%, var(--photo-light) 70%); }
  .cover__band { position: absolute; left: 110px; top: 158px; width: 196px; height: 32px;
    background: rgba(255,255,255,.92); display: flex; align-items: center; gap: 6px; padding-left: 6px; }
  .cover__dot { width: 22px; height: 22px; border-radius: 50%; background: var(--ink); flex: none; }
  .cover__title { line-height: 1; }
  .cover__name { font-size: 9.5px; font-weight: 700; color: var(--soft); display: block; }
  .cover__kit { font-size: 11px; font-weight: 900; color: var(--ink); display: block; text-align: right; padding-right: 4px; }

  /* about */
  .about__title { left: 128px; top: 20px; }
  .about__copy { left: 128px; top: 38px; width: 178px; }
  .vision__title { left: 14px; top: 172px; font-size: 10px; }
  .vision__copy { position: absolute; left: 14px; top: 190px; width: 64px; font-size: 8px; line-height: 1.05; font-weight: 700; color: var(--soft); }
  .vision__copy b { color: var(--ink); font-weight: 900; font-size: 7px; letter-spacing: .4px; }

  /* stats */
  .stats__title { left: 133px; top: 22px; }
  .stats__lead { position: absolute; left: 133px; top: 38px; width: 170px; font-size: 4.4px; line-height: 1.5; color: var(--muted); font-weight: 700; }
  .stats__lead b { color: var(--ink); font-size: 5.6px; font-weight: 900; }
  .stats__chart { position: absolute; inset: 0; }

  /* network & contact */
  .col { left: 124px; }
  .network__title { top: 16px; }
  .network__intro { top: 31px; width: 160px; }
  .network__list { position: absolute; left: 124px; top: 42px; list-style: none; font-size: 6px; line-height: 1.25; color: var(--muted); font-weight: 700; }
  .year__title { top: 112px; }
  .year__copy { top: 128px; width: 165px; }
  .contact__title { top: 16px; }
  .contact__sub { position: absolute; left: 124px; top: 30px; font-size: 6px; color: var(--soft); font-weight: 700; }
  .contact__list { position: absolute; left: 124px; top: 44px; font-size: 5.4px; line-height: 1.3; color: var(--muted); font-weight: 700; font-style: normal; }
</style>
</head>
<body>

<section class="page page--about" aria-label="Page 2: Who are we">
  <div class="brand"><span class="brand__dot"></span><span class="brand__name">the velvet quarter</span></div>
  <h2 class="heading about__title">Who Are We?</h2>
  <div class="copy about__copy">
    <p>The Velvet Quarter is all about the <b>lovely things in life</b></p>
    <p>It is the home for <b>delectable fashion</b>, <b>enviable interiors</b>, <b>inspired music</b> and <b>memorable travel experiences</b> to name just a few.</p>
    <p>Most of all however, it's about these things being <b>accessible to everyone</b></p>
    <p>That means that as <b>beautiful as the photos look</b>, we know most people can't really live with all white rooms. Or walk down the street wearing a nude tulle skirt.</p>
    <p>That said, there's no reason practicality means boring or ugly.</p>
    <p>Of course, like real lives, wardrobes, diets and MP3 players, at The <b>Velvet Quarter Laurent Vey</b> lives happily alongside Zenna, you'll see superfoods as well as sundaes and hear Lola Vance on the same playlist as Vinyl Frost.</p>
    <p>The Velvet Quarter is based in Melbourne, Australia and takes submissions and <b>content from all over the world</b></p>
    <p>With everything we do we always consider the fact that we live in an age where <b>people see</b>, <b>read</b>, <b>hear</b> and <b>experience things</b> that might be happening in the next street or on the other side of the world.</p>
    <p>This means that everything that appears in The Velvet Quarter is <b>meaningful</b> no matter where you <b>live</b>, <b>work</b> and <b>play</b></p>
  </div>
  <h2 class="heading vision__title">Our Vision</h2>
  <p class="vision__copy">The home of <b>accessible</b>, <b>inspiring</b> and <b>beautiful</b> <b>lifestyle</b> elements.</p>
</section>

<section class="page page--cover" aria-label="Page 1: Cover">
  <div class="cover__photo" role="img" aria-label="Studio group photograph of five young people in autumn fashion, one holding a small dog, against a pale grey backdrop"></div>
  <div class="cover__band">
    <span class="cover__dot"></span>
    <h1 class="cover__title">
      <span class="cover__name">the velvet quarter</span>
      <span class="cover__kit">media kit</span>
    </h1>
  </div>
</section>

<section class="page page--stats" aria-label="Page 3: The picture">
  <svg class="stats__chart" width="316" height="250" viewBox="0 0 316 250" aria-hidden="true">
    <circle cx="62" cy="125" r="44" fill="#d6d6d6"/>
    <circle cx="62" cy="132" r="25" fill="#111"/>
    <text x="62" y="123" text-anchor="middle" font-family="Playfair Display, serif" font-size="4.5" font-weight="700" fill="#fff">Up to</text>
    <text x="62" y="133" text-anchor="middle" font-family="Playfair Display, serif" font-size="9" font-weight="900" fill="#fff">3,500</text>
    <text x="62" y="139" text-anchor="middle" font-family="Playfair Display, serif" font-size="4.2" font-weight="700" fill="#fff">unique visitors</text>
    <text x="62" y="144" text-anchor="middle" font-family="Playfair Display, serif" font-size="4.2" font-weight="700" fill="#fff">each day</text>

    <text x="148" y="100" text-anchor="middle" font-family="Playfair Display, serif" font-size="4.5" font-weight="700" fill="#111">Average time on site</text>
    <rect x="118" y="104" width="60" height="38" rx="5" fill="#222"/>
    <rect x="122" y="108" width="52" height="30" rx="2" fill="#c8c8c8"/>
    <text x="148" y="129" text-anchor="middle" font-family="Playfair Display, serif" font-size="15" font-weight="900" fill="#111">04:30</text>

    <rect x="213" y="80" width="86" height="52" rx="3" fill="#222"/>
    <rect x="218" y="85" width="76" height="42" fill="#fff"/>
    <path d="M206 132 H306 L300 138 H212 Z" fill="#111"/>
    <text x="256" y="97" text-anchor="middle" font-family="Playfair Display, serif" font-size="4.5" font-weight="700" fill="#111">Average pages per visit</text>
    <text x="256" y="115" text-anchor="middle" font-family="Playfair Display, serif" font-size="13" font-weight="900" fill="#111">7.3</text>

    <circle cx="85" cy="195" r="16" fill="#111"/>
    <path d="M76 190 H86 V185 L95 195 L86 205 V200 H76 Z" fill="#fff"/>
    <text x="116" y="193" font-family="Playfair Display, serif" font-size="13" font-weight="900" fill="#111">38%</text>
    <text x="128" y="200" text-anchor="middle" font-family="Playfair Display, serif" font-size="4.2" font-weight="700" fill="#111">of readers</text>
    <text x="128" y="205" text-anchor="middle" font-family="Playfair Display, serif" font-size="4.2" font-weight="700" fill="#111">come back</text>
    <text x="130" y="213" text-anchor="middle" font-family="Playfair Display, serif" font-size="6.5" font-weight="900" fill="#111">3 or more times</text>
    <text x="130" y="219" text-anchor="middle" font-family="Playfair Display, serif" font-size="4.2" font-weight="700" fill="#111">a month</text>

    <circle cx="228" cy="190" r="32" fill="none" stroke="#cfcfcf" stroke-width="12"/>
    <path d="M228 158 A32 32 0 1 0 251 212" fill="none" stroke="#111" stroke-width="12"/>
    <text x="228" y="183" text-anchor="middle" font-family="Playfair Display, serif" font-size="4.2" font-weight="700" fill="#111">More than half</text>
    <text x="228" y="189" text-anchor="middle" font-family="Playfair Display, serif" font-size="4.2" font-weight="700" fill="#111">our traffic is made</text>
    <text x="228" y="195" text-anchor="middle" font-family="Playfair Display, serif" font-size="4.2" font-weight="700" fill="#111">up of</text>
    <text x="228" y="201" text-anchor="middle" font-family="Playfair Display, serif" font-size="4.2" font-weight="700" fill="#111">first time visitors</text>
  </svg>
  <div class="brand"><span class="brand__dot"></span><span class="brand__name">the velvet quarter</span></div>
  <h2 class="heading stats__title">The Picture</h2>
  <p class="stats__lead">The Velvet Quarter is very young, but we're <b>growing up fast</b><br>Our <b>readership</b> and reach <b>expands every day</b></p>
</section>

<section class="page page--network" aria-label="Page 4: Our network and the year ahead">
  <div class="brand"><span class="brand__dot"></span><span class="brand__name">the velvet quarter</span></div>
  <h2 class="heading col network__title">Our Network</h2>
  <p class="copy col network__intro">Some of our current and previous advertisers and affiliate partners include:</p>
  <ul class="network__list">
    <li>The Outlook Rail</li>
    <li>My Cupboard Co</li>
    <li>Pairings Fashion</li>
    <li>Cove Beauty</li>
    <li>Smedley &amp; Hart</li>
    <li>Adrian Wexley</li>
  </ul>
  <h2 class="heading col year__title">The Year Ahead</h2>
  <div class="copy col year__copy">
    <p>Establishment of contributor network to have <b>daily updates</b> in each major category.</p>
    <p>Launch our <b>weekly newsletter</b></p>
    <p>Develop <b>custom visual content.</b></p>
  </div>
</section>

<section class="page page--contact" aria-label="Page 5: Contact">
  <div class="brand"><span class="brand__dot"></span><span class="brand__name">the velvet quarter</span></div>
  <h2 class="heading col contact__title">Contact</h2>
  <p class="contact__sub">Press Releases &amp; Other Media Enquiries</p>
  <address class="contact__list">
    Sarah Holloway<br>
    sarah@thevelvetquarter.example<br>
    +61 (0) 400 000 123<br>
    www.thevelvetquarter.example
  </address>
</section>

</body>
</html>
```